Business Card Design Project

Colette Marivaux logo on front of card with 'of Sydney' added in small font.
Back of card needs to include the following information :

"Pure pleasure for the discerning gentleman" (I may omit once I've seen the design)

colettemarivaux.com.au

Contact by SMS or email only :

colette@colettemarivaux.com.au
Mobile : 0483 956 204 or + 61 483 956 204

Target Market(s)

Male professionals aged 20-60.

Industry/Entity Type

Business

Requirements
Must have
• Simple, bold, stylish and elegant.

```html
<!DOCTYPE html>
<html lang="en">
<head>
<meta charset="utf-8">
<title>Colette Marivaux — Business Card</title>
<link href="https://fonts.googleapis.com/css2?family=Open+Sans:wght@400;600&display=swap" rel="stylesheet">
<style>
  :root {
    --page-bg: #e7e4e0;
    --card-dark-top: #4a4846;
    --card-dark-top-end: #2f2e2d;
    --card-light-top: #e2e1df;
    --card-light-top-end: #c9c8c6;
    --band: #1d1c1c;
    --ink-light: #f4f2ef;
    --ink-soft: #d9d6d2;
    --ink-dark: #2a2928;
    --ink-dark-soft: #4a4846;
  }
  * { box-sizing: border-box; margin: 0; padding: 0; }
  html, body { width: 797px; height: 1200px; overflow: hidden; }
  body {
    background: var(--page-bg);
    font-family: "Open Sans", Arial, sans-serif;
    position: relative;
  }
  .card {
    position: absolute;
    left: 48px;
    width: 700px;
    height: 360px;
    border-radius: 16px;
    overflow: hidden;
    box-shadow: 0 14px 34px rgba(0,0,0,0.18);
  }
  .card--front { top: 150px; }
  .card--back  { top: 690px; }

  .card__face {
    position: absolute; left: 0; top: 0; width: 100%; height: 212px;
    display: flex; flex-direction: column; align-items: center; justify-content: center;
  }
  .card--front .card__face { background: linear-gradient(180deg, var(--card-dark-top), var(--card-dark-top-end)); }
  .card--back .card__face  { background: linear-gradient(180deg, var(--card-light-top), var(--card-light-top-end)); }

  .brand__name {
    font-weight: 400;
    font-size: 34px;
    letter-spacing: 6px;
    text-transform: uppercase;
    margin-top: 14px;
  }
  .brand__place {
    font-size: 13px;
    letter-spacing: 4px;
    text-transform: uppercase;
    margin-top: 16px;
  }
  .card--front .brand__name { color: var(--ink-light); }
  .card--front .brand__place { color: var(--ink-soft); }
  .card--back .brand__name { color: var(--ink-dark); }
  .card--back .brand__place { color: var(--ink-dark-soft); }

  .card__band {
    position: absolute; left: 0; top: 212px; width: 100%; height: 148px;
    background: var(--band);
    color: var(--ink-light);
  }
  .contact {
    position: absolute; left: 410px; top: 26px;
  }
  .contact__title { font-size: 17px; margin-bottom: 14px; }
  .contact__line {
    display: flex; align-items: center; gap: 12px;
    font-size: 12.5px; color: var(--ink-soft); margin-bottom: 9px;
  }
  .contact__line svg { width: 13px; height: 13px; flex: none; fill: var(--ink-soft); }
  .contact__sep { margin: 0 10px; }
  .website {
    position: absolute; left: 50px; bottom: 22px;
    font-size: 13px; color: var(--ink-soft);
  }
</style>
</head>
<body>

  <section class="card card--front">
    <div class="card__face">
      <div class="brand__name">Colette Marivaux</div>
      <div class="brand__place">of Sydney</div>
    </div>
    <div class="card__band">
      <div class="contact">
        <p class="contact__title">Contact by SMS or email only :</p>
        <p class="contact__line">
          <svg viewBox="0 0 16 16"><path d="M3.5 1.5l2.5 0 1.2 3.2-1.6 1.2c.8 1.8 2.2 3.2 4 4l1.2-1.6 3.2 1.2v2.5c0 .8-.7 1.5-1.5 1.5C7 13.5 2 8.5 2 3c0-.8.7-1.5 1.5-1.5z"/></svg>
          <span>0483 956 204<span class="contact__sep">-</span>+ 61 483 956 204</span>
        </p>
        <p class="contact__line">
          <svg viewBox="0 0 16 16"><path d="M1 3h14v10H1z M2 4l6 5 6-5" fill="none" stroke="#d9d6d2" stroke-width="1.4"/><rect x="1" y="3" width="14" height="10" fill="#d9d6d2" opacity="0.85"/><path d="M1.5 3.5l6.5 5 6.5-5" fill="none" stroke="#1d1c1c" stroke-width="1.3"/></svg>
          <span>colette@colettemarivaux.com.au</span>
        </p>
      </div>
      <p class="website">colettemarivaux.com.au</p>
    </div>
  </section>

  <section class="card card--back">
    <div class="card__face">
      <div class="brand__name">Colette Marivaux</div>
      <div class="brand__place">of Sydney</div>
    </div>
    <div class="card__band">
      <div class="contact">
        <p class="contact__title">Contact by SMS or email only :</p>
        <p class="contact__line">
          <svg viewBox="0 0 16 16"><path d="M3.5 1.5l2.5 0 1.2 3.2-1.6 1.2c.8 1.8 2.2 3.2 4 4l1.2-1.6 3.2 1.2v2.5c0 .8-.7 1.5-1.5 1.5C7 13.5 2 8.5 2 3c0-.8.7-1.5 1.5-1.5z"/></svg>
          <span>0483 956 204<span class="contact__sep">-</span>+ 61 483 956 204</span>
        </p>
        <p class="contact__line">
          <svg viewBox="0 0 16 16"><rect x="1" y="3" width="14" height="10" fill="#d9d6d2" opacity="0.85"/><path d="M1.5 3.5l6.5 5 6.5-5" fill="none" stroke="#1d1c1c" stroke-width="1.3"/></svg>
          <span>colette@colettemarivaux.com.au</span>
        </p>
      </div>
      <p class="website">colettemarivaux.com.au</p>
    </div>
  </section>

</body>
</html>
```